Legal Service Estimated Retainer and Average Case Value

We need an 11x14 flyer that contains the standard retainers and average cost be case, both provided in documents, for each case type we handle. We need the information displayed, preferably in a way that makes the information readable but less troubling to a client shocked at price of litigation. We need one sheet with the retainers and average case value merged into one table.

Target Market(s)

Potential Clients

Font styles to use
Serif
Sans Serif

```html
<!DOCTYPE html>
<html lang="en">
<head>
<meta charset="utf-8">
<title>Family Law Fee Flyer</title>
<link href="https://fonts.googleapis.com/css2?family=Libre+Baskerville:wght@400;700&family=Montserrat:wght@400;500;600;700&display=swap" rel="stylesheet">
<style>
:root{
  --navy:#0d1c52;
  --navy-mid:#173a9a;
  --blue-bright:#2450c0;
  --page-bg:#b4b4b4;
  --white:#ffffff;
  --panel:#f1f1f1;
  --pill:#c9c9c9;
  --rule:#c4c4c4;
  --grey-text:#7a7a7a;
  --ink:#1f2340;
}
*{margin:0;padding:0;box-sizing:border-box}
html,body{width:800px;height:1200px;overflow:hidden}
body{background:var(--page-bg);font-family:"Montserrat",Arial,sans-serif;position:relative}
.flyer{position:absolute;left:0;top:91px;width:800px;height:1018px;background:var(--white);overflow:hidden}
.hero-art{position:absolute;left:0;top:0;width:800px;height:372px}
.brand{position:absolute;left:48px;top:44px;display:flex;align-items:center;gap:10px}
.brand-square{width:14px;height:14px;background:var(--navy)}
.brand-name{font-family:"Libre Baskerville",Georgia,serif;font-size:19px;color:var(--navy);letter-spacing:.5px}
.headline{position:absolute;left:40px;top:125px;color:var(--white);font-family:"Libre Baskerville",Georgia,serif;line-height:1.1}
.headline .small{font-size:31px;display:block;letter-spacing:.5px}
.headline .big{font-size:54px;font-weight:700;display:block;margin-top:2px}
.hero-rule{position:absolute;left:40px;top:272px;width:326px;height:1px;background:rgba(255,255,255,.7)}
.hero-rule::before{content:"";position:absolute;left:0;top:-2px;width:72px;height:5px;border-radius:3px;background:var(--white)}
.hero-intro{position:absolute;left:40px;top:283px;width:370px;color:var(--white);font-size:13.2px;line-height:1.1}
.band-line{position:absolute;left:0;top:376px;width:800px;height:5px;background:var(--rule)}
.section-title{position:absolute;font-family:"Libre Baskerville",Georgia,serif;font-size:20px;line-height:1.35;color:var(--navy);font-weight:700}
.section-title .light{color:var(--grey-text);font-weight:400}
.fees-title{left:39px;top:404px}
.retainers-title{left:422px;top:400px}
.title-rule{position:absolute;height:1px;background:var(--rule)}
.title-rule::before{content:"";position:absolute;left:0;top:-2px;width:38px;height:5px;border-radius:3px;background:var(--navy)}
.fees-rule{left:39px;top:434px;width:330px}
.retainers-rule{left:422px;top:464px;width:200px}
.fees-intro{position:absolute;left:38px;top:452px;width:335px;font-size:8.6px;line-height:1.25;color:#444}
.rate-panel{position:absolute;background:var(--panel);padding:16px 10px 14px 10px;display:flex;flex-direction:column;justify-content:space-between}
.fees-panel{left:38px;top:516px;width:345px;height:435px}
.retainers-panel{left:421px;top:486px;width:345px;height:465px;padding:26px 15px 20px 15px}
.rate-row{display:flex;align-items:center;justify-content:space-between}
.rate-label{display:flex;align-items:flex-start;gap:10px;font-size:11.3px;font-weight:600;color:var(--ink);line-height:1.15}
.rate-label::before{content:"";flex:none;width:7px;height:7px;margin-top:3px;background:var(--navy)}
.rate-pill{flex:none;width:94px;height:12px;background:var(--pill);font-size:7.2px;font-weight:700;color:var(--white);text-align:center;line-height:12px}
.footer-line{position:absolute;left:0;top:959px;width:800px;height:4px;background:var(--rule)}
.footer{position:absolute;left:0;top:964px;width:800px;height:54px;background:var(--navy);display:flex;align-items:center;color:var(--white)}
.contact{display:flex;align-items:center;gap:10px}
.contact-phone{margin-left:50px;font-size:21px;font-weight:700;letter-spacing:.3px}
.contact-address{font-size:11px;line-height:1.2}
.contact-web{font-size:12px}
.divider{width:1px;height:22px;background:var(--white);margin:0 24px}
</style>
</head>
<body>
<main class="flyer">
  <svg class="hero-art" viewBox="0 0 800 372" xmlns="http://www.w3.org/2000/svg">
    <defs>
      <radialGradient id="bandGlow" cx="0.5" cy="0.55" r="0.7">
        <stop offset="0" stop-color="#2352c4"/>
        <stop offset="0.55" stop-color="#15348f"/>
        <stop offset="1" stop-color="#0c1d5c"/>
      </radialGradient>
      <linearGradient id="portraitTone" x1="0" y1="0" x2="0" y2="1">
        <stop offset="0" stop-color="#1a3f9e"/>
        <stop offset="0.55" stop-color="#1b2f6e"/>
        <stop offset="1" stop-color="#14204a"/>
      </linearGradient>
    </defs>
    <path d="M0 100 L330 100 C372 100 382 31 432 31 L800 31 L800 372 L0 372 Z" fill="url(#bandGlow)"/>
    <path d="M316 97 C362 94 372 31 424 31 L446 31 C398 36 384 100 332 100 Z" fill="#c6c6c6"/>
    <rect x="421" y="31" width="379" height="341" fill="url(#portraitTone)" role="img" aria-label="Portrait photo of the attorney in a dark suit and tie, smiling"/>
  </svg>

  <div class="brand">
    <span class="brand-square"></span>
    <span class="brand-name">DANIEL M WHITFORD</span>
  </div>

  <h1 class="headline">
    <span class="small">CENTRAL PA'S</span>
    <span class="small">PREMIER FAMILY</span>
    <span class="big">LAW FIRM</span>
  </h1>
  <div class="hero-rule"></div>
  <p class="hero-intro">The Law Office of Daniel M. Whitford is a different type of law firm that offers clients guidance with their lives, not just legal help. If you are facing a divorce or family law issue, we are ready to assist in a resolution.</p>
  <div class="band-line"></div>

  <h2 class="section-title fees-title"><span class="light">AVERAGE</span> FEE PER CASE TYPE</h2>
  <div class="title-rule fees-rule"></div>
  <p class="fees-intro">In order for our clients to set expectations for legal fees, we provide the national average range of fees per case type. These are only to provide you with an understanding of what other cases have cost clients in similar cases. Please note these are not estimates nor guarantees of your own legal costs.</p>

  <section class="rate-panel fees-panel">
    <div class="rate-row"><span class="rate-label">Custody Contempt/Modification</span><span class="rate-pill">$5,000 - $8,000</span></div>
    <div class="rate-row"><span class="rate-label">Custody Initial Order</span><span class="rate-pill">$4,000 - $7,000</span></div>
    <div class="rate-row"><span class="rate-label">Custody &amp; Support</span><span class="rate-pill">$5,000 - $8,000</span></div>
    <div class="rate-row"><span class="rate-label">Support $2,000</span><span class="rate-pill">$2,000 - $4,000</span></div>
    <div class="rate-row"><span class="rate-label">Divorce (3301c)</span><span class="rate-pill">$1,500 - $3,000</span></div>
    <div class="rate-row"><span class="rate-label">Divorce (3301d)</span><span class="rate-pill">$2,000 - $3,000</span></div>
    <div class="rate-row"><span class="rate-label">Protection from Abuse</span><span class="rate-pill">$1,500 - $3,000</span></div>
    <div class="rate-row"><span class="rate-label">Divorce &amp; Custody</span><span class="rate-pill">$5,000 - $8,000</span></div>
    <div class="rate-row"><span class="rate-label">Divorce &amp; Equitable<br>Distribution</span><span class="rate-pill">$6,000 - $10,000</span></div>
    <div class="rate-row"><span class="rate-label">Divorce, Custody<br>&amp; Support</span><span class="rate-pill">$8,000 - $12,000</span></div>
    <div class="rate-row"><span class="rate-label">Divorce, Equitabl<br>Distribution &amp; Custody</span><span class="rate-pill">$10,000 - $15,000</span></div>
    <div class="rate-row"><span class="rate-label">Divorce, Equitable<br>Distribution &amp; Support</span><span class="rate-pill">$8,000 - $12,000</span></div>
    <div class="rate-row"><span class="rate-label">Divorce, Equitable Distribution<br>Custody &amp; Support</span><span class="rate-pill">$12,000 - $15,000</span></div>
  </section>

  <h2 class="section-title retainers-title"><span class="light">RETAINERS AND TOTAL</span><br>ESTIMATED CASE COSTS</h2>
  <div class="title-rule retainers-rule"></div>

  <section class="rate-panel retainers-panel">
    <div class="rate-row"><span class="rate-label">Divorce (3301 C): Retainer</span><span class="rate-pill">$2,000</span></div>
    <div class="rate-row"><span class="rate-label">Divorce (3301 D): Retainer</span><span class="rate-pill">$2,500</span></div>
    <div class="rate-row"><span class="rate-label">Divorce and Custody: Retainer</span><span class="rate-pill">$3,500</span></div>
    <div class="rate-row"><span class="rate-label">Divorce and Equitable<br>Distribution:Retainer</span><span class="rate-pill">$3,500</span></div>
    <div class="rate-row"><span class="rate-label">Divorce and Support:<br>Retainer</span><span class="rate-pill">$3,000</span></div>
    <div class="rate-row"><span class="rate-label">Divorce, Custody and<br>Support: Retainer</span><span class="rate-pill">$3,500</span></div>
    <div class="rate-row"><span class="rate-label">Divorce, Equitable Distribution<br>and Support: Retainer</span><span class="rate-pill">$3,500</span></div>
    <div class="rate-row"><span class="rate-label">Divorce, Equitable Distribution<br>and Custody: Retainer</span><span class="rate-pill">$5,000</span></div>
    <div class="rate-row"><span class="rate-label">Divorce, Equitable Distribution,<br>Custody and Support: Retainer</span><span class="rate-pill">$3,500</span></div>
    <div class="rate-row"><span class="rate-label">Custody Initial Order: Retainer</span><span class="rate-pill">$3,000</span></div>
    <div class="rate-row"><span class="rate-label">Custody Modification: Retainer</span><span class="rate-pill">$3,500</span></div>
    <div class="rate-row"><span class="rate-label">Custody and Support: Retainer</span><span class="rate-pill">$3,000</span></div>
    <div class="rate-row"><span class="rate-label">(PFA) Protection From Abuse</span><span class="rate-pill">$2,000 Paid in Full</span></div>
  </section>

  <div class="footer-line"></div>
  <footer class="footer">
    <div class="contact contact-phone">
      <svg width="22" height="22" viewBox="0 0 24 24" aria-hidden="true"><path d="M6.6 10.8a15.1 15.1 0 0 0 6.6 6.6l2.2-2.2a1 1 0 0 1 1-.25 11.4 11.4 0 0 0 3.6.57 1 1 0 0 1 1 1V20a1 1 0 0 1-1 1A17 17 0 0 1 3 4a1 1 0 0 1 1-1h3.5a1 1 0 0 1 1 1c0 1.25.2 2.45.57 3.57a1 1 0 0 1-.25 1z" fill="none" stroke="#fff" stroke-width="1.8"/></svg>
      <span>(717) 555-0143</span>
    </div>
    <span class="divider"></span>
    <div class="contact contact-address">
      <svg width="14" height="20" viewBox="0 0 14 20" aria-hidden="true"><path d="M7 0a7 7 0 0 0-7 7c0 5 7 13 7 13s7-8 7-13a7 7 0 0 0-7-7zm0 9.6A2.6 2.6 0 1 1 7 4.4a2.6 2.6 0 0 1 0 5.2z" fill="#fff"/></svg>
      <span>2150 Ridgeview Avenue Suite 210,<br>Harrisburg, PA 17110</span>
    </div>
    <span class="divider"></span>
    <div class="contact contact-web">
      <svg width="14" height="14" viewBox="0 0 16 16" aria-hidden="true"><g fill="none" stroke="#fff" stroke-width="1.3"><circle cx="8" cy="8" r="7"/><ellipse cx="8" cy="8" rx="3" ry="7"/><path d="M1 8h14M2.2 4.3h11.6M2.2 11.7h11.6"/></g></svg>
      <span>www.whitfordfamilylaw.com</span>
    </div>
  </footer>
</main>
</body>
</html>
```